Quorvilan Mobile App

We are in need of a design for a mobile application that delivers relevant content to users based on the profile that they enter and based on the answers that they enter in a daily health tracker. There also will be functionality that will allow a user to check the cost of a medical service/ procedure before going to the medical provider (could get a list of providers and costs after entering procedure, service or prescription in a search box). The content will be articles or information that our team will find/develop on a daily basis and put into a database that the app will pull off of. The profile needs to capture age, sex, ethinicity (optional) and then have a list of topics that the user can select to get daily updated information/content. These topics are: Diabetes, Heart Disease, Hypertension, COPD, Back Pain, Weight Management, Depression, Cancer, Wellness Plan. The final design should allow for users to receive helpful health care information every day based on their profile and the answers in the daily health tracker.

Medical

```html
<!DOCTYPE html>
<html lang="en">
<head>
<meta charset="utf-8">
<title>Quorvilan Mobile App Screens</title>
<link href="https://fonts.googleapis.com/css2?family=Lato:wght@300;400;700&display=swap" rel="stylesheet">
<style>
:root{
  --bg:#0b1a3f;
  --blue:#3bb4e5;
  --green:#7dc242;
  --text:#4a4a4a;
  --muted:#9a9a9a;
  --line:#e4e4e4;
  --white:#ffffff;
  --row-hi:#efefef;
}
*{box-sizing:border-box;margin:0;padding:0}
html,body{width:1200px;height:1200px;overflow:hidden}
body{background:var(--bg);font-family:'Lato',sans-serif;position:relative;color:var(--text)}

.app-icon{position:absolute;left:30px;top:35px;width:170px;height:168px;border-radius:26px;
  background:linear-gradient(#fbfbfb,#ebebe9);display:flex;align-items:center;justify-content:center}
.app-icon .brand{font-size:27px;font-weight:700;color:var(--blue)}

.screen{position:absolute;background:var(--white);overflow:hidden}
.screen.main{width:246px;height:435px;top:121px}
.splash{left:248px;background:radial-gradient(circle at 50% 45%,#ffffff 30%,#d6d6d6 100%);display:flex;align-items:center;justify-content:center}
.splash .brand{font-size:34px;font-weight:700;color:var(--blue)}
.user-list{left:550px}
.user-profile{left:866px}

.status{height:16px;background:var(--blue);color:var(--white);font-size:7px;display:flex;align-items:center;justify-content:space-between;padding:0 6px}
.header{height:30px;background:var(--blue);color:var(--white);display:flex;align-items:center;justify-content:center;position:relative;font-size:15px;font-weight:300;letter-spacing:.5px}
.back{position:absolute;left:8px;top:8px;width:14px;height:14px}

.row{height:43.5px;display:flex;align-items:center;padding:0 10px;border-bottom:1px solid var(--line)}
.row.active{background:var(--row-hi)}
.row .avatar{width:28px;height:28px;border-radius:50%;background:linear-gradient(135deg,#8fb6d8,#c9a48a);margin-right:12px;flex:none}
.row .txt{flex:1}
.row .title{font-size:11px;color:var(--muted)}
.row .sub{font-size:8.5px;color:#c2c2c2}
.row svg{width:8px;height:10px}

.profile-photo{height:250px;background:linear-gradient(180deg,#c9b89a 0%,#8c98a8 55%,#6f6a62 100%)}
.profile-info{position:absolute;left:0;right:0;top:278px;bottom:0;background:#58606e;color:var(--white);text-align:center}
.profile-avatar{position:absolute;left:147px;top:236px;width:78px;height:78px;border-radius:50%;border:3px solid var(--blue);background:linear-gradient(135deg,#5b7187,#2e3a46);z-index:2}
.profile-name{margin-top:47px;font-size:19px;font-weight:300}
.profile-url{font-size:8.5px;opacity:.85;margin-top:4px}
.profile-stats{display:flex;justify-content:center;gap:26px;font-size:8.5px;margin-top:10px}
.profile-stats span{display:flex;align-items:center;gap:4px}
.profile-stats svg{width:11px;height:11px}

.tracker{width:246px;transform-origin:0 0}
.tracker-a{left:270px;top:736px;height:437px;transform:scale(.833)}
.tracker-b{left:539px;top:683px;height:568px;transform:scale(.821)}
.q{padding:7px 10px 6px;border-bottom:1px solid var(--line)}
.q-text{font-size:9.5px;color:var(--text);line-height:1.25;margin-bottom:5px}
.opts{display:flex;align-items:center;gap:6px;font-size:7.5px;color:var(--muted)}
.opt{display:flex;align-items:center;gap:4px}
.opt.on{color:var(--text)}
.radio{width:14px;height:14px;border-radius:50%;border:1px solid #aaa;display:inline-block}
.opt.on .radio{border:none;background:var(--green);display:flex;align-items:center;justify-content:center}
.radio svg{width:9px;height:9px}
.entry{font-size:7.5px;color:var(--muted);display:flex;align-items:center;gap:4px}
.entry .box{width:36px;height:11px;border:1px solid #888;font-size:6px;text-align:right;padding-right:2px;color:var(--text)}
.btn{display:block;margin:8px auto 0;width:170px;height:28px;line-height:28px;text-align:center;color:var(--white);font-size:9.5px}
.btn.green{background:var(--green);border-bottom:2px solid #5e9a2f}
.btn.blue{background:var(--blue);border-bottom:2px solid #2a8fbb}
</style>
</head>
<body>

<div class="app-icon"><span class="brand">Quorvilan</span></div>

<div class="screen main splash"><span class="brand">Quorvilan</span></div>

<div class="screen main user-list">
  <div class="status"><span>NOVA ◠</span><span>4:21 PM</span><span>100% ▬</span></div>
  <div class="header">
    <svg class="back" viewBox="0 0 14 14"><circle cx="7" cy="7" r="6" fill="none" stroke="#fff" stroke-width="1.2"/><path d="M8 4 5 7l3 3" fill="none" stroke="#fff" stroke-width="1.3"/></svg>
    USER LIST
  </div>
  <div class="row"><div class="avatar" role="img" aria-label="User avatar photo"></div><div class="txt"><div class="title">Lorem Ipsum dolor com</div><div class="sub">lorem ipsum dol</div></div><svg viewBox="0 0 8 10"><path d="M2 1l4 4-4 4" fill="none" stroke="#888" stroke-width="1.3"/></svg></div>
  <div class="row"><div class="avatar" role="img" aria-label="User avatar photo"></div><div class="txt"><div class="title">Lorem Ipsum dolor com</div><div class="sub">lorem ipsum dol</div></div><svg viewBox="0 0 8 10"><path d="M2 1l4 4-4 4" fill="none" stroke="#888" stroke-width="1.3"/></svg></div>
  <div class="row"><div class="avatar" role="img" aria-label="User avatar photo"></div><div class="txt"><div class="title">Lorem Ipsum dolor com</div><div class="sub">lorem ipsum dol</div></div><svg viewBox="0 0 8 10"><path d="M2 1l4 4-4 4" fill="none" stroke="#888" stroke-width="1.3"/></svg></div>
  <div class="row"><div class="avatar" role="img" aria-label="User avatar photo"></div><div class="txt"><div class="title">Lorem Ipsum dolor com</div><div class="sub">lorem ipsum dol</div></div><svg viewBox="0 0 8 10"><path d="M2 1l4 4-4 4" fill="none" stroke="#888" stroke-width="1.3"/></svg></div>
  <div class="row active"><div class="avatar" role="img" aria-label="User avatar photo"></div><div class="txt"><div class="title">Lorem Ipsum dolor com</div><div class="sub">lorem ipsum dol</div></div><svg viewBox="0 0 8 10"><path d="M2 1l4 4-4 4" fill="none" stroke="#888" stroke-width="1.3"/></svg></div>
  <div class="row"><div class="avatar" role="img" aria-label="User avatar photo"></div><div class="txt"><div class="title">Lorem Ipsum dolor com</div><div class="sub">lorem ipsum dol</div></div><svg viewBox="0 0 8 10"><path d="M2 1l4 4-4 4" fill="none" stroke="#888" stroke-width="1.3"/></svg></div>
  <div class="row"><div class="avatar" role="img" aria-label="User avatar photo"></div><div class="txt"><div class="title">Lorem Ipsum dolor com</div><div class="sub">lorem ipsum dol</div></div><svg viewBox="0 0 8 10"><path d="M2 1l4 4-4 4" fill="none" stroke="#888" stroke-width="1.3"/></svg></div>
  <div class="row"><div class="avatar" role="img" aria-label="User avatar photo"></div><div class="txt"><div class="title">Lorem Ipsum dolor com</div><div class="sub">lorem ipsum dol</div></div><svg viewBox="0 0 8 10"><path d="M2 1l4 4-4 4" fill="none" stroke="#888" stroke-width="1.3"/></svg></div>
  <div class="row"><div class="avatar" role="img" aria-label="User avatar photo"></div><div class="txt"><div class="title">Lorem Ipsum dolor com</div><div class="sub">lorem ipsum dol</div></div><svg viewBox="0 0 8 10"><path d="M2 1l4 4-4 4" fill="none" stroke="#888" stroke-width="1.3"/></svg></div>
</div>

<div class="screen main user-profile">
  <div class="status"><span>NOVA ◠</span><span>4:21 PM</span><span>100% ▬</span></div>
  <div class="header">
    <svg class="back" viewBox="0 0 14 14"><circle cx="7" cy="7" r="6" fill="none" stroke="#fff" stroke-width="1.2"/><path d="M8 4 5 7l3 3" fill="none" stroke="#fff" stroke-width="1.3"/></svg>
    USER PRIFILE
  </div>
  <div class="profile-photo" role="img" aria-label="Cover photo of a photographer on rocks above a misty mountain landscape"></div>
  <div class="profile-avatar" role="img" aria-label="Profile portrait photo"></div>
  <div class="profile-info">
    <div class="profile-name">Marek Olsen</div>
    <div class="profile-url">m.quorvilan.app</div>
    <div class="profile-stats">
      <span><svg viewBox="0 0 12 12"><circle cx="6" cy="6" r="5" fill="none" stroke="#fff"/><path d="M6 3v3l2 1" fill="none" stroke="#fff"/></svg>18.07.13</span>
      <span><svg viewBox="0 0 12 12"><path d="M6 10 1.5 5.5A2.5 2.5 0 0 1 6 2.8a2.5 2.5 0 0 1 4.5 2.7z" fill="none" stroke="#fff"/></svg>324</span>
      <span><svg viewBox="0 0 12 12"><path d="M2 2h8v6H5l-3 2z" fill="none" stroke="#fff"/></svg>26</span>
    </div>
  </div>
</div>

<div class="screen tracker tracker-a">
  <div class="status"><span>NOVA ◠</span><span>4:21 PM</span><span>100% ▬</span></div>
  <div class="header">
    <svg class="back" viewBox="0 0 14 14"><circle cx="7" cy="7" r="6" fill="none" stroke="#fff" stroke-width="1.2"/><path d="M8 4 5 7l3 3" fill="none" stroke="#fff" stroke-width="1.3"/></svg>
    Quorvilan
  </div>
  <div class="q"><div class="q-text">How many hours did you sleep last night?</div><div class="opts"><span class="opt"><span class="radio"></span>Less than 6 hours</span><span class="opt on"><span class="radio"><svg viewBox="0 0 10 10"><path d="M2 5l2 2 4-4" fill="none" stroke="#fff" stroke-width="1.6"/></svg></span>More than 6 hours</span></div></div>
  <div class="q"><div class="q-text">Have you exercised today?</div><div class="opts"><span class="opt"><span class="radio"></span>Yes</span><span class="opt on"><span class="radio"><svg viewBox="0 0 10 10"><path d="M2 5l2 2 4-4" fill="none" stroke="#fff" stroke-width="1.6"/></svg></span>No</span></div></div>
  <div class="q"><div class="q-text">Have you had a cigarette today?</div><div class="opts"><span class="opt"><span class="radio"></span>Yes</span><span class="opt on"><span class="radio"><svg viewBox="0 0 10 10"><path d="M2 5l2 2 4-4" fill="none" stroke="#fff" stroke-width="1.6"/></svg></span>No</span></div></div>
  <div class="q"><div class="q-text">Have you had any alcoholic beverages today?</div><div class="opts"><span class="opt"><span class="radio"></span>Yes</span><span class="opt on"><span class="radio"><svg viewBox="0 0 10 10"><path d="M2 5l2 2 4-4" fill="none" stroke="#fff" stroke-width="1.6"/></svg></span>No</span></div></div>
  <div class="q"><div class="q-text">How would you describe your eating over the last 24 hours?</div><div class="opts"><span class="opt"><span class="radio"></span>Healthy</span><span class="opt on"><span class="radio"><svg viewBox="0 0 10 10"><path d="M2 5l2 2 4-4" fill="none" stroke="#fff" stroke-width="1.6"/></svg></span>Not bad</span><span class="opt on"><span class="radio"><svg viewBox="0 0 10 10"><path d="M2 5l2 2 4-4" fill="none" stroke="#fff" stroke-width="1.6"/></svg></span>Needs Improvement</span></div></div>
  <div class="q"><div class="q-text">How would you describe your stress level over the last 24 hours?</div><div class="opts"><span class="opt"><span class="radio"></span>Low/None</span><span class="opt on"><span class="radio"><svg viewBox="0 0 10 10"><path d="M2 5l2 2 4-4" fill="none" stroke="#fff" stroke-width="1.6"/></svg></span>Slightly Elevated</span><span class="opt on"><span class="radio"><svg viewBox="0 0 10 10"><path d="M2 5l2 2 4-4" fill="none" stroke="#fff" stroke-width="1.6"/></svg></span>High</span></div></div>
  <div class="q" style="border:none"><div class="q-text">Have you checked your insulin levels today?</div><div class="entry">If yes, enter results here: <span class="box">#</span></div></div>
  <span class="btn green">Submit to Your Health Tracker</span>
</div>

<div class="screen tracker tracker-b">
  <div class="status"><span>NOVA ◠</span><span>4:21 PM</span><span>100% ▬</span></div>
  <div class="header">
    <svg class="back" viewBox="0 0 14 14"><circle cx="7" cy="7" r="6" fill="none" stroke="#fff" stroke-width="1.2"/><path d="M8 4 5 7l3 3" fill="none" stroke="#fff" stroke-width="1.3"/></svg>
    Quorvilan
  </div>
  <div class="q"><div class="q-text">How many hours did you sleep last night?</div><div class="opts"><span class="opt"><span class="radio"></span>Less than 6 hours</span><span class="opt on"><span class="radio"><svg viewBox="0 0 10 10"><path d="M2 5l2 2 4-4" fill="none" stroke="#fff" stroke-width="1.6"/></svg></span>More than 6 hours</span></div></div>
  <div class="q"><div class="q-text">Have you exercised today?</div><div class="opts"><span class="opt"><span class="radio"></span>Yes</span><span class="opt on"><span class="radio"><svg viewBox="0 0 10 10"><path d="M2 5l2 2 4-4" fill="none" stroke="#fff" stroke-width="1.6"/></svg></span>No</span></div></div>
  <div class="q"><div class="q-text">Have you had a cigarette today?</div><div class="opts"><span class="opt"><span class="radio"></span>Yes</span><span class="opt on"><span class="radio"><svg viewBox="0 0 10 10"><path d="M2 5l2 2 4-4" fill="none" stroke="#fff" stroke-width="1.6"/></svg></span>No</span></div></div>
  <div class="q"><div class="q-text">Have you had any alcoholic beverages today?</div><div class="opts"><span class="opt"><span class="radio"></span>Yes</span><span class="opt on"><span class="radio"><svg viewBox="0 0 10 10"><path d="M2 5l2 2 4-4" fill="none" stroke="#fff" stroke-width="1.6"/></svg></span>No</span></div></div>
  <div class="q"><div class="q-text">How would you describe your eating over the last 24 hours?</div><div class="opts"><span class="opt"><span class="radio"></span>Healthy</span><span class="opt on"><span class="radio"><svg viewBox="0 0 10 10"><path d="M2 5l2 2 4-4" fill="none" stroke="#fff" stroke-width="1.6"/></svg></span>Not bad</span><span class="opt on"><span class="radio"><svg viewBox="0 0 10 10"><path d="M2 5l2 2 4-4" fill="none" stroke="#fff" stroke-width="1.6"/></svg></span>Needs Improvement</span></div></div>
  <div class="q"><div class="q-text">How would you describe your stress level over the last 24 hours?</div><div class="opts"><span class="opt"><span class="radio"></span>Low/None</span><span class="opt on"><span class="radio"><svg viewBox="0 0 10 10"><path d="M2 5l2 2 4-4" fill="none" stroke="#fff" stroke-width="1.6"/></svg></span>Slightly Elevated</span><span class="opt on"><span class="radio"><svg viewBox="0 0 10 10"><path d="M2 5l2 2 4-4" fill="none" stroke="#fff" stroke-width="1.6"/></svg></span>High</span></div></div>
  <div class="q" style="border:none"><div class="q-text">Have you checked your insulin levels today?</div><div class="entry">If yes, enter results here: <span class="box">#</span></div></div>
  <span class="btn green">Submit to Your Health Tracker</span>
  <span class="btn blue">Email Report</span>
  <div class="q" style="border:none;margin-top:6px"><div class="q-text">Have you taken all prescribed medicines as instructed in the last 24 hours?</div><div class="opts"><span class="opt"><span class="radio"></span>Yes</span><span class="opt on"><span class="radio"><svg viewBox="0 0 10 10"><path d="M2 5l2 2 4-4" fill="none" stroke="#fff" stroke-width="1.6"/></svg></span>No</span></div></div>
</div>

</body>
</html>
```